Innovative, creative, and beautiful simple book cover!

I’ve spend 5 years writing a book about executive consulting. Last task of the project is to find the best possible cover and I need help from you guys.

In the book, I take the liberty of creating a model which secures successful sales throughout the value chain, driven by the top management.

For you info, I used Pixel Harbor once before and of cause ended buying a logo. In short I’m here to buy the best book cover idea - and look forward to see what genius ideas you can bring to the table.

Thank you very much.
Torvald

P.S. Please see my brief in attach documents. .
Updates

Target Market(s)

Business people en general

Industry/Entity Type

Management Consulting

Font styles to use
Sans Serif

Requirements
Must have
• - My attach files about description for front page and back page have to be incorporated.
• - BOTH A FRONT, SPINE AND A BACK PAGE!
• - Please see all my attach files – the project is very well described and should be ready to work on.
• - The idea about the “building line” is an idea I love, but if you have something else you think I should see – try me.
Nice to have
• I love simple, minimalistic design
Should not have
• I don't like old fashion or over designed solutions. Sorry :-)

```html
<!DOCTYPE html>
<html lang="en">
<head>
<meta charset="utf-8">
<title>Boardroom Sales Strategy – Book Cover</title>
<link rel="stylesheet" href="https://fonts.googleapis.com/css2?family=Work+Sans:wght@200;300;400&family=Roboto+Condensed:wght@300;400&family=Roboto:wght@400;700&display=swap">
<style>
  :root {
    --page-bg: #e6e6e6;
    --cover-front: #2f88c9;
    --cover-spine: #2b7dbd;
    --cover-back: #2a77b6;
    --text-light: #ffffff;
    --text-soft: #e4f0fa;
    --text-navy: #14345c;
    --glow: #dcebf7;
    --skyline: #c8def0;
    --photo-dark: #3a3a3a;
    --photo-light: #8a8a8a;
  }
  * { box-sizing: border-box; margin: 0; padding: 0; }
  html, body { width: 1200px; height: 877px; overflow: hidden; background: var(--page-bg); }
  .canvas { position: relative; width: 1200px; height: 877px; }

  .book-jacket {
    position: absolute; left: 44px; top: 58px;
    display: flex; height: 760px;
    box-shadow: 0 14px 40px rgba(0,0,0,0.18);
  }

  /* Back cover */
  .back-cover {
    width: 520px; height: 100%;
    background: var(--cover-back);
    padding: 44px 34px;
    font-family: "Roboto", sans-serif;
    color: var(--text-soft);
    font-size: 14px; line-height: 1.42;
  }
  .author-intro { display: flex; gap: 18px; }
  .author-photo {
    flex: 0 0 150px; height: 270px;
    background: linear-gradient(160deg, var(--photo-light), var(--photo-dark));
    border: 3px solid #9aa3ab;
  }
  .bio-lead strong { color: var(--text-light); font-weight: 700; }
  .bio-lead p + p { margin-top: 18px; }
  .bio-more { margin-top: 12px; }

  /* Spine */
  .spine {
    width: 84px; height: 100%;
    background: linear-gradient(90deg, var(--cover-back), var(--cover-spine) 40%, var(--cover-front));
    position: relative; overflow: hidden;
  }
  .spine-title, .spine-author {
    position: absolute; left: 50%;
    transform-origin: left top;
    white-space: nowrap; color: var(--text-light);
  }
  .spine-title {
    top: 36px; transform: rotate(90deg) translateY(-50%);
    font-family: "Work Sans", sans-serif; font-weight: 200; font-size: 40px;
  }
  .spine-author {
    top: 545px; transform: rotate(90deg) translateY(-50%);
    font-family: "Roboto Condensed", sans-serif; font-weight: 400; font-size: 28px;
  }

  /* Front cover */
  .front-cover {
    position: relative; width: 520px; height: 100%;
    background: var(--cover-front);
    overflow: hidden;
  }
  .skyline {
    position: absolute; left: 0; right: 0; top: 300px; height: 360px;
    background: linear-gradient(180deg,
      rgba(200,222,240,0) 0%,
      rgba(200,222,240,0.5) 40%,
      var(--skyline) 70%,
      rgba(200,222,240,0.6) 88%,
      rgba(200,222,240,0) 100%);
  }
  .front-glow {
    position: absolute; left: -80px; right: -80px; top: 500px; height: 300px;
    background: radial-gradient(ellipse at center, rgba(220,235,247,0.85) 0%, rgba(220,235,247,0.45) 40%, rgba(47,136,201,0) 72%);
  }
  .book-title {
    position: absolute; left: 38px; top: 46px;
    font-family: "Work Sans", sans-serif; font-weight: 200;
    font-size: 84px; line-height: 1.08; color: var(--text-light);
    letter-spacing: -1px;
  }
  .tagline {
    position: absolute; left: 30px; right: 30px; top: 576px;
    font-family: "Roboto", sans-serif; font-size: 19px; line-height: 1.3;
    color: var(--text-navy); text-align: center;
  }
  .byline {
    position: absolute; left: 0; right: 0; top: 664px; text-align: center;
    color: var(--text-light); font-family: "Roboto Condensed", sans-serif;
  }
  .byline-label { font-size: 14px; font-weight: 300; }
  .byline-name { font-size: 42px; font-weight: 400; line-height: 1.05; }
</style>
</head>
<body>
<main class="canvas">
  <div class="book-jacket">
    <section class="back-cover">
      <div class="author-intro">
        <div class="author-photo" role="img" aria-label="Black and white portrait photo of the author"></div>
        <div class="bio-lead">
          <p><strong>Torvald Brekke</strong>'s career has been enriched by 10 years as a hardcore salesman and sales manager, followed by 10 years of top management in the advertising business and advisor within the Embassy Foreign Services.</p>
          <p>He has worked with 300 companies in more than 10 different countries, amongst them several top world brands.</p>
        </div>
      </div>
      <p class="bio-more">Lived in Copenhagen, London and Dubai, guest lectured at Nordhavn University, chaired an international Advisory Board with high profiled business people and obtained an Executive Master of Business Administration in Strategic Management as well as a top Governance Board Education.</p>
    </section>

    <section class="spine">
      <span class="spine-title">Boardroom Sales Strategy</span>
      <span class="spine-author">Torvald Brekke</span>
    </section>

    <section class="front-cover">
      <div class="skyline" role="img" aria-label="City skyline silhouette of towers and landmark buildings"></div>
      <div class="front-glow"></div>
      <h1 class="book-title">Boardroom<br>Sales<br>Strategy</h1>
      <p class="tagline">In this book, i take the liberty of creating a model wich secures successful sales throughout the value chain, driven by the top management</p>
      <div class="byline">
        <div class="byline-label">Written by</div>
        <div class="byline-name">Torvald Brekke</div>
      </div>
    </section>
  </div>
</main>
</body>
</html>
```